Portfolio required for virtual assistant seeking new clients

I require an editable Word template that can be sent to clients. This is a new business venture I am undertaking - working as a virtual assistant (administration work). I will need to find my own clients so would like Wow factor. Target group will be small businesses/legal industry so needs to look professional.
The portfolio will need to note information about me, why hire me, my skill set and credentials. May add testimonials too. I have attached a draft of the amount of text required - still working on this.
I will upload my logo and business card design. I do like consistency.
Colours used Pantone 2745 C and 272 C. Open to other colours but would like to see the main colours of logo incorporated. Images welcome. May insert an image of myself at some stage so please allow for a spot for this photo.
The portfolio will need to be converted to pdf to send by email as well as printable.
Updates

Automatically set for 24 hours apologies did not see this. Now amended

```html
<!DOCTYPE html>
<html lang="en">
<head>
<meta charset="utf-8">
<title>Virtual Assistant Portfolio – Mara Quill</title>
<link href="https://fonts.googleapis.com/css2?family=Montserrat:wght@300;400;500;600;700;800&display=swap" rel="stylesheet">
<style>
  :root {
    --navy: #2b3784;
    --periwinkle: #7485c2;
    --lavender: #a0a9d6;
    --mist: #c8cde8;
    --haze: #e3e1ee;
    --frost: #eef0f8;
    --ink: #1f1f2b;
    --body: #3a3a46;
    --muted: #6b6d7a;
    --backdrop: #b0b0b0;
    --white: #ffffff;
  }
  * { margin: 0; padding: 0; box-sizing: border-box; }
  html, body { width: 1200px; height: 2365px; overflow: hidden; background: var(--backdrop); }
  body { font-family: "Montserrat", sans-serif; color: var(--body); }

  .sheet {
    position: absolute; left: 0; top: 0;
    width: 1307px; height: 2576px;
    transform: scale(0.91813); transform-origin: 0 0;
  }
  .spread { position: absolute; left: 107px; width: 1097px; height: 775px; }
  .spread--cover { top: 90px; }
  .spread--intro { top: 891px; }
  .spread--skills { top: 1693px; }
  .page { position: absolute; top: 0; width: 548px; height: 775px; background: var(--white); overflow: hidden; }
  .page--left { left: 0; }
  .page--right { left: 549px; }
  .fold { position: absolute; left: 548px; top: 0; width: 1px; height: 775px; background: #c9c9c9; }
  .spread--cover .page { background: var(--navy); }
  .spread--cover .fold { background: #4a56a0; }

  /* Cover */
  .brand-name { color: var(--periwinkle); font-weight: 600; text-align: center; width: 100%; position: absolute; left: 0; letter-spacing: 0.5px; }
  .back-cover .brand-name { top: 222px; font-size: 30px; }
  .front-cover .brand-name { top: 255px; font-size: 62px; }
  .back-cover .contact-stack { position: absolute; left: 0; width: 100%; text-align: center; color: var(--white); }
  .contact-kicker { top: 346px; font-size: 23px; font-weight: 300; text-decoration: underline; text-underline-offset: 4px; }
  .contact-title { top: 376px; font-size: 23px; font-weight: 600; }
  .contact-name { top: 421px; font-size: 14px; line-height: 19px; font-weight: 400; letter-spacing: 0.3px; }
  .contact-icon { width: 16px; height: 16px; left: 266px; position: absolute; }
  .contact-line { font-size: 15px; }
  .front-cover .cover-title { position: absolute; left: 0; width: 100%; text-align: center; color: var(--white); }
  .cover-title__lead { top: 408px; font-size: 34px; font-weight: 300; letter-spacing: 0.5px; }
  .cover-title__main { top: 448px; font-size: 38px; font-weight: 800; letter-spacing: 1px; }
  .cover-contacts { position: absolute; top: 518px; left: 0; width: 100%; display: flex; justify-content: center; gap: 36px; color: var(--white); font-size: 13px; }
  .cover-contacts span { display: inline-flex; align-items: center; gap: 5px; }

  /* Shared interior */
  .tile { position: absolute; }
  .tile--periwinkle { background: var(--periwinkle); }
  .tile--lavender { background: var(--lavender); }
  .tile--mist { background: var(--mist); }
  .tile--haze { background: var(--haze); }
  .tile--frost { background: var(--frost); }
  .tile--navy { background: var(--navy); }

  .page-heading { position: absolute; color: var(--ink); font-size: 31px; line-height: 38px; font-weight: 400; letter-spacing: 0.3px; white-space: nowrap; }
  .page-heading b { font-weight: 800; }

  .lead { position: absolute; color: var(--navy); font-weight: 500; }
  .copy { position: absolute; font-size: 10.6px; line-height: 13.8px; color: var(--body); }

  .folio { position: absolute; top: 723px; display: flex; align-items: center; gap: 6px; font-size: 7.5px; color: var(--navy); letter-spacing: 0.2px; }
  .folio b { font-weight: 700; }
  .folio__num { width: 20px; height: 18px; background: var(--mist); display: flex; align-items: center; justify-content: center; font-size: 8px; color: var(--navy); }
  .folio--left { left: 34px; }
  .folio--right { right: 34px; }
  .folio-mark { position: absolute; top: 743px; width: 11px; height: 11px; background: var(--navy); }

  /* About */
  .about-banner { position: absolute; left: 34px; top: 134px; width: 248px; height: 59px; background: var(--navy); color: var(--white); font-size: 31px; line-height: 59px; padding-left: 17px; letter-spacing: 0.5px; }
  .about-banner b { font-weight: 800; }
  .contact-inline { position: absolute; display: flex; align-items: center; gap: 5px; color: var(--navy); font-size: 12.5px; }

  /* Why hire */
  .illustration { position: absolute; left: 0; top: 214px; width: 548px; height: 273px; background: linear-gradient(180deg, #e4e6f2 0%, #e4e6f2 78%, var(--periwinkle) 78%, var(--periwinkle) 100%); }

  /* Skills */
  .skill-col { position: absolute; top: 263px; }
  .skill-col--left { left: 33px; width: 220px; }
  .skill-col--right { left: 283px; width: 232px; }
  .skill-group { margin-bottom: 21px; }
  .skill-group h3 { color: var(--navy); font-size: 13.8px; line-height: 16px; font-weight: 700; margin-bottom: 13px; }
  .skill-group ul { list-style: none; font-size: 10.8px; line-height: 12px; color: var(--muted); }
  .skill-group li { padding-left: 9px; text-indent: -9px; }
  .skill-group li::before { content: "• "; }

  .credential-list { position: absolute; left: 34px; top: 268px; list-style: none; font-size: 11px; color: var(--muted); }
  .credential-list li { height: 24px; }
  .credential-list li::before { content: "• "; }
</style>
</head>
<body>
<div class="sheet">

  <!-- Cover spread -->
  <section class="spread spread--cover">
    <div class="page page--left back-cover">
      <div class="brand-name">Mara Quill</div>
      <div class="contact-stack contact-kicker">Now</div>
      <div class="contact-stack contact-title">Contact Me</div>
      <div class="contact-stack contact-name">MARA QUILL<br>VIRTUAL ASSISTANT</div>
      <svg class="contact-icon" style="top:481px" viewBox="0 0 16 16" fill="none" stroke="#fff" stroke-width="1.1"><rect x="1.5" y="3.5" width="13" height="9"/><path d="M1.5 3.5 8 9l6.5-5.5M1.5 12.5 6 8M14.5 12.5 10 8"/></svg>
      <div class="contact-stack contact-line" style="top:499px">mara@mqva.com.au</div>
      <svg class="contact-icon" style="top:546px" viewBox="0 0 16 16" fill="none" stroke="#fff" stroke-width="1.1"><path d="M4 2 6.2 4.6 5 6.3c.8 1.7 2.2 3.1 3.9 3.9l1.7-1.2L13.2 11l-.9 2.3c-4.6.1-9.5-4.8-9.4-9.4z"/><path d="M9.5 2.5a4 4 0 0 1 4 4M9.5 4.5a2 2 0 0 1 2 2"/></svg>
      <div class="contact-stack contact-line" style="top:564px">0491 570 118</div>
    </div>
    <div class="fold"></div>
    <div class="page page--right front-cover">
      <div class="brand-name">Mara Quill</div>
      <div class="cover-title cover-title__lead">VIRTUAL ASSISTANT</div>
      <div class="cover-title cover-title__main">PORTFOLIO</div>
      <div class="cover-contacts">
        <span><svg width="16" height="14" viewBox="0 0 16 14" fill="none" stroke="#fff" stroke-width="1.1"><rect x="1" y="2" width="14" height="10"/><path d="M1 2l7 6 7-6M1 12l5-4.5M15 12l-5-4.5"/></svg>mara@mqva.com.au</span>
        <span><svg width="14" height="14" viewBox="0 0 16 16" fill="none" stroke="#fff" stroke-width="1.2"><path d="M4 2 6.2 4.6 5 6.3c.8 1.7 2.2 3.1 3.9 3.9l1.7-1.2L13.2 11l-.9 2.3c-4.6.1-9.5-4.8-9.4-9.4z"/></svg>0491 570 118</span>
      </div>
    </div>
  </section>

  <!-- About / Why hire spread -->
  <section class="spread spread--intro">
    <div class="page page--left about-page">
      <div class="tile tile--periwinkle" style="left:237px;top:0;width:278px;height:307px"></div>
      <div class="about-banner"><b>ABOUT</b> ME</div>
      <p class="lead" style="left:34px;top:349px;width:470px;font-size:14.6px;line-height:17.6px">Hello, I’m Mara Quill, a mother, coffee lover, and a passion for travel. I enjoy organisation and making life easy. With over 15 years of experience in the legal field, I have gained valuable experience whilst at the same time, perfecting my skills.</p>
      <p class="copy" style="left:34px;top:454px;width:236px">Throughout my journey in the legal profession, I have held various roles, each contributing to my growth and expertise. Starting as a Rounds Clerk, I quickly advanced to the role of Administrative Assistant in the area of Litigation which involved leading a team of administration assistants focused on supporting legal professionals and litigation processes. This role was invaluable in that it taught me the importance of organisation, time management, attention to detail and multitasking.</p>
      <p class="copy" style="left:283px;top:454px;width:236px">I then transitioned into Debt Recovery, where I thrived as a Paralegal. In this role, I took on the responsibility of managing my own caseload and providing comprehensive legal support independently. Attention to detail, meticulous research and effective communication became second nature. This allowed me to achieve successful resolutions while maintaining the utmost organization and professionalism.</p>
      <div class="contact-inline" style="left:283px;top:641px"><svg width="15" height="15" viewBox="0 0 16 16" fill="none" stroke="#2b3784" stroke-width="1.2"><path d="M4 2 6.2 4.6 5 6.3c.8 1.7 2.2 3.1 3.9 3.9l1.7-1.2L13.2 11l-.9 2.3c-4.6.1-9.5-4.8-9.4-9.4z"/><path d="M9.5 2.5a4 4 0 0 1 4 4M9.5 4.5a2 2 0 0 1 2 2"/></svg>0491 570 118</div>
      <div class="contact-inline" style="left:283px;top:666px"><svg width="16" height="13" viewBox="0 0 16 14" fill="none" stroke="#2b3784" stroke-width="1.2"><rect x="1" y="2" width="14" height="10"/><path d="M1 2l7 6 7-6M1 12l5-4.5M15 12l-5-4.5"/></svg>mara@mqva.com.au</div>
      <div class="folio folio--left"><span class="folio__num">2</span><span><b>VIRTUAL</b> ASSISTANT</span></div>
      <div class="folio-mark" style="left:21px"></div>
    </div>
    <div class="fold"></div>
    <div class="page page--right why-page">
      <div class="tile tile--periwinkle" style="left:271px;top:0;width:93px;height:73px"></div>
      <div class="tile tile--lavender" style="left:369px;top:0;width:87px;height:73px"></div>
      <div class="tile tile--mist" style="left:461px;top:0;width:87px;height:73px"></div>
      <div class="tile tile--mist" style="left:369px;top:77px;width:87px;height:80px"></div>
      <div class="tile tile--haze" style="left:461px;top:77px;width:87px;height:80px"></div>
      <div class="tile tile--navy" style="left:45px;top:98px;width:19px;height:19px"></div>
      <div class="tile tile--mist" style="left:66px;top:119px;width:68px;height:67px"></div>
      <h2 class="page-heading" style="left:77px;top:134px"><b>WHY</b> HIRE ME?</h2>
      <div class="illustration" role="img" aria-label="Illustration of a virtual assistant wearing a headset, working at a desk with a computer between two potted plants"></div>
      <div class="tile tile--frost" style="left:461px;top:162px;width:87px;height:82px"></div>
      <p class="lead" style="left:33px;top:513px;width:490px;font-size:10.8px;line-height:13.7px">A virtual assistant is an affordable alternative to hiring on-site administration support. Hire me for a once-off task or on a regular basis. I’m here to help you so get more time back in your day so you can focus on more important tasks. I want to save you time, as who has enough of that these days!</p>
      <p class="copy" style="left:33px;top:592px;width:226px">I am known for my reliability, determination, ability to work diligently in fast-paced environments as well as delivering results. I take pride in my meticulous approach to the tasks I undertake. I adapt well to new technology.</p>
      <p class="copy" style="left:278px;top:592px;width:240px">I am excited to embrace new opportunities that allow me to showcase my skill set expertise, provide dedicated support to professionals and that may involve my legal expertise. I am committed to making a positive impact wherever I go, bringing efficiency and structure.</p>
      <div class="folio folio--right"><span><b>VIRTUAL</b> ASSISTANT</span><span class="folio__num">3</span></div>
      <div class="folio-mark" style="left:515px"></div>
    </div>
  </section>

  <!-- Skills / Credentials spread -->
  <section class="spread spread--skills">
    <div class="page page--left skills-page">
      <div class="tile tile--mist" style="left:329px;top:34px;width:86px;height:81px"></div>
      <div class="tile tile--lavender" style="left:420px;top:34px;width:94px;height:81px"></div>
      <div class="tile tile--periwinkle" style="left:420px;top:120px;width:94px;height:80px"></div>
      <div class="tile tile--navy" style="left:34px;top:89px;width:19px;height:19px"></div>
      <div class="tile tile--mist" style="left:55px;top:110px;width:68px;height:67px"></div>
      <h2 class="page-heading" style="left:66px;top:126px"><b>WHAT</b> CAN I DO</h2>
      <h2 class="page-heading" style="left:142px;top:164px">FOR YOU?</h2>

      <div class="skill-col skill-col--left">
        <div class="skill-group">
          <h3>GENERAL ADMINISTRATION<br>SUPPORT</h3>
          <ul>
            <li>Document preparation including editing and formatting</li>
            <li>Spreadsheets</li>
            <li>Client correspondence</li>
            <li>Customer service / telephone calls</li>
            <li>Invoicing</li>
            <li>Bulk mail outs</li>
            <li>Data entry</li>
            <li>Database and records management</li>
          </ul>
        </div>
        <div class="skill-group">
          <h3>Email management</h3>
          <ul>
            <li>Categorize and prepare sub folders</li>
            <li>Prioritize emails</li>
            <li>Send email correspondence</li>
          </ul>
        </div>
        <div class="skill-group">
          <h3>Calendar &amp; diary management</h3>
          <ul>
            <li>Assist with scheduling appointments and meetings</li>
            <li>Scheduling reminders</li>
          </ul>
        </div>
        <div class="skill-group">
          <h3>Travel arrangements</h3>
          <ul>
            <li>Assist with booking intrastate/interstate travel</li>
            <li>Assist with car hire and accommodation</li>
          </ul>
        </div>
      </div>

      <div class="skill-col skill-col--right">
        <div class="skill-group">
          <h3>Software</h3>
          <ul>
            <li>Tallyset 365</li>
            <li>Brieflane Practice</li>
            <li>Quirefold</li>
          </ul>
        </div>
        <div class="skill-group">
          <h3>Debt Collection</h3>
          <ul>
            <li>Assist with sending out overdue statements</li>
            <li>Issue demand letters</li>
            <li>Issue Claims and enforcement action in the Magistrates Court of the State</li>
            <li>Negotiating payment arrangements</li>
            <li>Knowledge with Lodgewick portal</li>
          </ul>
        </div>
        <div class="skill-group">
          <h3>Other</h3>
          <ul>
            <li>Online research</li>
            <li>Event coordination</li>
          </ul>
        </div>
        <div class="skill-group">
          <h3>Legal</h3>
          <ul>
            <li>Lodgewick portal</li>
            <li>Preparing Court documents</li>
            <li>Filing Court Documents</li>
          </ul>
        </div>
      </div>

      <div class="folio folio--left"><span class="folio__num">4</span><span><b>VIRTUAL</b> ASSISTANT</span></div>
      <div class="folio-mark" style="left:21px"></div>
    </div>
    <div class="fold"></div>
    <div class="page page--right credentials-page">
      <div class="tile tile--navy" style="left:34px;top:89px;width:19px;height:19px"></div>
      <div class="tile tile--mist" style="left:55px;top:110px;width:68px;height:67px"></div>
      <h2 class="page-heading" style="left:66px;top:126px"><b>CREDENTIALS</b></h2>
      <ul class="credential-list">
        <li>Certificate IV in Business (Legal Services)</li>
        <li>Certificate III of Business Administration</li>
        <li>Certificate II in Business</li>
      </ul>
      <div class="tile tile--periwinkle" style="left:458px;top:359px;width:90px;height:80px"></div>
      <div class="tile tile--periwinkle" style="left:167px;top:442px;width:94px;height:80px"></div>
      <div class="tile tile--mist" style="left:367px;top:444px;width:87px;height:80px"></div>
      <div class="tile tile--lavender" style="left:458px;top:444px;width:90px;height:80px"></div>
      <div class="tile tile--mist" style="left:68px;top:529px;width:94px;height:81px"></div>
      <div class="tile tile--frost" style="left:269px;top:529px;width:94px;height:81px"></div>
      <div class="tile tile--haze" style="left:367px;top:529px;width:87px;height:81px"></div>
      <div class="tile tile--mist" style="left:458px;top:529px;width:90px;height:81px"></div>
      <div class="tile tile--mist" style="left:172px;top:615px;width:87px;height:82px"></div>
      <div class="tile tile--lavender" style="left:269px;top:615px;width:94px;height:82px"></div>
      <div class="folio folio--right"><span><b>VIRTUAL</b> ASSISTANT</span><span class="folio__num">5</span></div>
      <div class="folio-mark" style="left:515px"></div>
    </div>
  </section>

</div>
</body>
</html>
```